Business Cards and Stationery for Mobile Ultrasound
Redfern Harbor Mobile Ultrasound
Business Cards and Stationery for Mobile Ultrasound - Medical
Creative Brief
Professional
Marovic Deltrane
P.O Box 827 Quenton CA 95871
mar@rhqx.example
rhqx.example

```html
<!DOCTYPE html>
<html lang="en">
<head>
<meta charset="utf-8">
<title>Redfern Harbor Mobile Ultrasound – Business Card</title>
<link rel="stylesheet" href="https://fonts.googleapis.com/css2?family=Open+Sans:wght@400;600&display=swap">
<style>
  :root {
    --bg: #3b3b3d;
    --purple: #5a1f9c;
    --purple-deep: #47157f;
    --white: #ffffff;
    --ink: #555a60;
    --line: #b9a6d6;
  }
  html, body {
    margin: 0;
    width: 1200px;
    height: 901px;
    overflow: hidden;
    background: var(--bg);
    font-family: "Open Sans", Arial, sans-serif;
  }
  .stage {
    position: relative;
    width: 1200px;
    height: 901px;
    display: flex;
    align-items: center;
    justify-content: center;
    gap: 50px;
  }
  .card {
    position: relative;
    width: 540px;
    height: 310px;
    border-radius: 18px;
    overflow: hidden;
    box-shadow: 0 12px 30px rgba(0,0,0,.35);
  }
  .card-back {
    background: linear-gradient(135deg, var(--purple) 0%, var(--purple-deep) 100%);
    display: flex;
    align-items: center;
    justify-content: center;
  }
  .brand {
    font-weight: 600;
    line-height: 1.15;
    text-align: center;
  }
  .card-back .brand {
    color: var(--white);
    font-size: 26px;
  }
  .brand small {
    display: block;
    font-size: .5em;
    letter-spacing: 3px;
    text-transform: uppercase;
  }
  .card-front { background: var(--purple); }
  .card-front .shape { position: absolute; inset: 0; }
  .card-front .brand {
    position: absolute;
    left: 34px;
    top: 44px;
    color: var(--purple);
    font-size: 22px;
    text-align: left;
  }
  .holder {
    position: absolute;
    right: 30px;
    top: 128px;
    color: var(--white);
    font-size: 16px;
    font-weight: 600;
    white-space: nowrap;
  }
  .contact {
    position: absolute;
    left: 34px;
    top: 130px;
    margin: 0;
    padding: 0;
    list-style: none;
    color: var(--ink);
    font-size: 11.5px;
    line-height: 1.45;
  }
  .contact .row { display: flex; align-items: center; gap: 7px; margin-top: 3px; }
  .contact .icon { width: 11px; height: 11px; flex: none; }
</style>
</head>
<body>
<main class="stage">
  <section class="card card-back">
    <div class="brand">Redfern Harbor<small>Mobile Ultrasound</small></div>
  </section>

  <section class="card card-front">
    <svg class="shape" viewBox="0 0 540 310" aria-hidden="true">
      <path d="M0 0 H150 C320 30 350 200 260 310 H0 Z" fill="#ffffff"/>
      <path d="M164 2 C334 34 364 204 274 310" fill="none" stroke="#b9a6d6" stroke-width="2"/>
      <line x1="34" y1="286" x2="240" y2="286" stroke="#b9a6d6" stroke-width="1"/>
    </svg>
    <div class="brand">Redfern Harbor<small>Mobile Ultrasound</small></div>
    <ul class="contact">
      <li>P.O Box 827</li>
      <li>Quenton CA 95871</li>
      <li class="row">
        <svg class="icon" viewBox="0 0 12 12"><circle cx="6" cy="6" r="6" fill="#5a1f9c"/><path d="M4 3.2 L5 5 L4.4 5.6 Q5.3 7 6.6 7.7 L7.2 7 L8.9 8 L8.3 9 Q5.8 9.2 3.5 5.4 Z" fill="#fff"/></svg>
        209.555.0147
      </li>
      <li class="row">
        <svg class="icon" viewBox="0 0 12 12"><circle cx="6" cy="6" r="6" fill="#5a1f9c"/><rect x="3" y="4" width="6" height="4.2" fill="none" stroke="#fff" stroke-width=".9"/><path d="M3 4 L6 6.4 L9 4" fill="none" stroke="#fff" stroke-width=".9"/></svg>
        mar@rhqx.example
      </li>
      <li class="row">
        <svg class="icon" viewBox="0 0 12 12"><circle cx="6" cy="6" r="6" fill="#5a1f9c"/><circle cx="6" cy="6" r="3" fill="none" stroke="#fff" stroke-width=".9"/><line x1="3" y1="6" x2="9" y2="6" stroke="#fff" stroke-width=".8"/></svg>
        rhqx.example
      </li>
    </ul>
    <div class="holder">Marovic Deltrane</div>
  </section>
</main>
</body>
</html>
```